Stationery Design Project

We need a stationery design to change our look to a more corporate design. My company has been established since 1989 and over that time has changed from your average sign company to doing more Corporate re branding projects and have some multi National clients.
Our website is currently being redesigned so we need a new logo and business cards etc. to compliment it.
I have 2 graphic designers employed but i want on outsiders opinion and a totally independant view point.
Updates
Hi Designers
We are predominantely a sign manufacturing company that manufacturers every type of sign you can imagine. However the majoprity of our work is digital graphics. Our claim to faim is that we wrap the Harbourtown Skytrams and Cityglides which everyone seems to know in Sydney.We also do all sorts of Large format digital printing, vehicle wraps,vinyl signage,LED & Neon Illuminated signage,CNC Routing all materials,Laser cutting and Engraving, Architectural signage, Cut Out letters and Screenprinting.
Aswell as this we totally re-brand companies with internal wall graphics reception signage way finding signage and the like.We are a medium size company that has been trading since 1989 and has some very large reputable clients.
Our Company name is Brackwell Pty Ltd but like to have Signage and Graphics in our stationery.
Our details are as follows T: 9381 5027 F: 9381 5093 Unit 4, 22 Tallowood Lane.Kenbury Flats. NSW 2163 email mail@brackwellsigns.example our current website is being re-designed www.brackwellsigns.example
The design and colour scheme i would like is quite simple with a corporate feel and blue, grey & magenta are colours that seem to suit but am open to most suggestions just looking for clean lines.
Hopefully this is enough information if you require any more please ask.
Regards Dennis Albrook
Reason: I did not supply much information at first
Reason: I have extended it due to Christmas holidays
We are looking to simplify our LOGO not too concerned yet about layout of stationery items that we can easily work on later. I want to get a new logo that we can work with before we return to work on the 16th January so please concentrate on just the logo for now.
We would like to have Signs & Graphics somewhere in the name even though our registered name is Brackwell Pty Ltd. Brackwell is one word, i want it to be quite a bold font with no seriffs.The bright blue and grey colours are favourites so far with maybe a little magenta added later. Would like to have a Logo that is totally seperate and then the Brackwell P/L Signs & graphics as a secondary item just to let people know what Brackwell do as the name obviously does not say what we are about.
Also we need to consider how we can put logo on T-shirts work shirts and company vehicles.
We do not need CD cover or envelopes but letterheads and business cards.
Reason: I want everyone to concentrate on a logo we return to work on the 16th of January so would like to have at least a logo approved by then
Reason: We are close to making a decision and just need a few more days for a couple of designers to submit extra things we have asked of them.
Business

```html
<!DOCTYPE html>
<html lang="en">
<head>
<meta charset="utf-8">
<title>Brackwell Pty Ltd – Stationery</title>
<link rel="stylesheet" href="https://fonts.googleapis.com/css2?family=Arimo:wght@400;700&display=swap">
<style>
  :root {
    --brand-blue: #1ea3dc;
    --brand-magenta: #e5358a;
    --brand-yellow: #ffe12b;
    --brand-grey: #8c8c8c;
    --ink: #555555;
    --paper: #ffffff;
    --backdrop: #4a4a4a;
  }
  * { box-sizing: border-box; margin: 0; padding: 0; }
  html, body {
    width: 1200px; height: 900px; overflow: hidden;
    background: var(--backdrop);
    font-family: "Arimo", Arial, sans-serif;
    color: var(--ink);
  }
  .canvas { position: relative; width: 1200px; height: 900px; }

  /* Brand lock-up: name + tagline */
  .brand { position: absolute; display: flex; flex-direction: column; align-items: flex-start; }
  .brand--centered { left: 0; right: 0; align-items: center; }
  .wordmark {
    display: flex; align-items: center; gap: 0.3em;
    font-weight: 700; color: var(--brand-blue);
    text-transform: uppercase; letter-spacing: 0.02em; white-space: nowrap; line-height: 1;
  }
  .wordmark__square { width: 0.8em; height: 0.8em; background: var(--brand-blue); flex: none; }
  .tagline {
    font-weight: 400; color: var(--brand-grey); text-transform: uppercase;
    letter-spacing: 0.3em; white-space: nowrap; line-height: 1; margin-top: 0.35em;
    padding-left: 1.9em;
  }

  /* Cover sheet */
  .cover-sheet {
    position: absolute; left: 38px; top: 106px; width: 485px; height: 684px;
    background: var(--paper); overflow: hidden;
  }
  .cover-sheet .brand { top: 388px; }
  .cover-sheet .wordmark { font-size: 31px; }
  .cover-sheet .tagline { font-size: 14px; }
  .footer-band {
    position: absolute; left: 0; right: 0; bottom: 0; height: 25px;
    display: flex; background: var(--brand-blue);
  }
  .footer-band__url {
    flex: 1; color: var(--paper); font-size: 14px; letter-spacing: 0.22em;
    line-height: 25px; padding-left: 62px; white-space: nowrap;
  }
  .chip { width: 29px; height: 25px; flex: none; }
  .chip--magenta { background: var(--brand-magenta); }
  .chip--yellow { background: var(--brand-yellow); }
  .chip--grey { background: var(--brand-grey); }

  /* Letterhead */
  .letterhead {
    position: absolute; left: 533px; top: 106px; width: 439px; height: 684px;
    background: var(--paper);
  }
  .letterhead .brand { left: 20px; top: 46px; }
  .letterhead .wordmark { font-size: 15px; }
  .letterhead .tagline { font-size: 7px; }
  .letterhead__contact {
    position: absolute; left: 288px; top: 38px; font-style: normal;
    font-size: 8px; line-height: 11.5px; color: var(--ink); white-space: nowrap;
  }
  .letterhead .footer-band__fill { flex: 1; background: var(--brand-blue); }

  /* Business cards */
  .card { position: absolute; background: var(--paper); border-radius: 10px; overflow: hidden; }
  .card--front { left: 605px; top: 259px; width: 383px; height: 216px; }
  .card--front .brand { top: 124px; }
  .card--front .wordmark { font-size: 17px; }
  .card--front .tagline { font-size: 8px; }
  .card__band { position: absolute; left: 0; right: 0; bottom: 0; height: 12px; background: var(--brand-blue); }

  .card--back { left: 785px; top: 489px; width: 381px; height: 219px; }
  .card--back .brand { left: 26px; top: 30px; }
  .card--back .wordmark { font-size: 15px; }
  .card--back .tagline { font-size: 7px; }
  .card__details {
    position: absolute; left: 0; right: 0; top: 89px; bottom: 0;
    background: var(--brand-blue); color: var(--paper);
    display: flex; padding: 22px 0 0 26px; font-size: 9px; line-height: 13px;
  }
  .card__notch {
    position: absolute; left: 20px; top: -10px; width: 0; height: 0;
    border-left: 10px solid transparent; border-right: 10px solid transparent;
    border-bottom: 10px solid var(--brand-blue);
  }
  .card__person { width: 190px; }
  .card__name { font-weight: 700; font-size: 11px; margin-bottom: 4px; }
  .card__role { margin-bottom: 16px; }
  .card__lines { border-left: 1px solid rgba(255,255,255,0.7); padding-left: 10px; white-space: nowrap; }
  .card__lines .gap { height: 12px; }
</style>
</head>
<body>
<main class="canvas">

  <section class="cover-sheet" aria-label="Cover sheet">
    <div class="brand brand--centered">
      <div class="wordmark"><span class="wordmark__square"></span>Brackwell Pty Ltd</div>
      <p class="tagline">Signs &amp; Graphics</p>
    </div>
    <div class="footer-band">
      <p class="footer-band__url">www.brackwellsigns.example</p>
      <span class="chip chip--magenta"></span>
      <span class="chip chip--yellow"></span>
      <span class="chip chip--grey"></span>
    </div>
  </section>

  <section class="letterhead" aria-label="Letterhead">
    <div class="brand">
      <div class="wordmark"><span class="wordmark__square"></span>Brackwell Pty Ltd</div>
      <p class="tagline">Signs &amp; Graphics</p>
    </div>
    <address class="letterhead__contact">
      Unit 4, 22 Tallowood Lane.<br>
      Kenbury Flats. NSW 2163 T: 9381 5027<br>
      F: 9381 5093<br>
      E: mail@brackwellsigns.example<br>
      www.brackwellsigns.example
    </address>
    <div class="footer-band">
      <span class="chip chip--grey"></span>
      <span class="chip chip--yellow"></span>
      <span class="chip chip--magenta"></span>
      <span class="footer-band__fill"></span>
    </div>
  </section>

  <section class="card card--front" aria-label="Business card front">
    <div class="brand brand--centered">
      <div class="wordmark"><span class="wordmark__square"></span>Brackwell Pty Ltd</div>
      <p class="tagline">Signs &amp; Graphics</p>
    </div>
    <span class="card__band"></span>
  </section>

  <section class="card card--back" aria-label="Business card back">
    <div class="brand">
      <div class="wordmark"><span class="wordmark__square"></span>Brackwell Pty Ltd</div>
      <p class="tagline">Signs &amp; Graphics</p>
    </div>
    <div class="card__details">
      <span class="card__notch"></span>
      <div class="card__person">
        <p class="card__name">Brackwell Pty Ltd</p>
        <p class="card__role">Position</p>
        <p>Unit 4, 22 Tallowood Lane.<br>Kenbury Flats. NSW 2163</p>
      </div>
      <div class="card__lines">
        <p>T: 9381 5027</p>
        <p>F: 9381 5093</p>
        <div class="gap"></div>
        <p>E: mail@brackwellsigns.example</p>
        <p><strong>www.brackwellsigns.example</strong></p>
      </div>
    </div>
  </section>

</main>
</body>
</html>
```